I need a audit of my current site.. with suggestions and actions

My current site, www.quillbarndocs does not support the high tech industry we are in. I am seeking knowledge, direction and action, I will pay hourly or by job. I also need SEO help, driven with impact trusted deliverable, our clients have to trust us to do our job. We are like Vornik to the construction industry, gathering their data for the lifecycle. Eliminating litigation, un wanted change orders and providing audit ready projects. Eveyone wins

Target Market(s)

Construction industry, Federal and Private

Industry/Entity Type

Construction industry, globally

Coding

Coded - Design and coding required

Number of Pages Required

5+ page

Font styles to use
Sans Serif

Colors
EE7325
F08F49
F5BC92
FAE3D3
FDF4ED

Requirements
Must have
• High tech look
Should not have
• Misspelled words

```html
<!DOCTYPE html>
<html lang="en">
<head>
<meta charset="utf-8">
<title>QuillbarnDocs — Construction Management Software</title>
<link href="https://fonts.googleapis.com/css2?family=Oswald:wght@400;500;600&family=Poppins:wght@300;400;500;600&display=swap" rel="stylesheet">
<style>
:root{
  --orange:#EE7325;
  --orange-2:#F08F49;
  --orange-3:#F5BC92;
  --orange-4:#FAE3D3;
  --orange-5:#FDF4ED;
  --ink:#1f1f1f;
  --text:#666;
  --light:#f4f4f4;
  --line:#e6e6e6;
  --dark:#2a2a2a;
  --darker:#222;
  --head:'Oswald',sans-serif;
  --body:'Poppins',sans-serif;
}
*{box-sizing:border-box;margin:0;padding:0}
html,body{width:1200px;height:4633px;overflow:hidden}
body{font-family:var(--body);color:var(--text);background:#fff;position:relative}
.section{position:absolute;left:0;width:1200px}
.abs{position:absolute}
.center{left:0;width:1200px;text-align:center}
.eyebrow{font-family:var(--body);font-size:9px;letter-spacing:3px;color:var(--orange);font-weight:500;text-transform:uppercase}
.h2{font-family:var(--head);font-weight:500;font-size:33px;line-height:38px;color:var(--ink);text-transform:uppercase}
.h2 .accent{color:var(--orange)}
.btn{display:inline-block;background:var(--orange);color:#fff;font-size:9px;font-weight:600;letter-spacing:1px;text-transform:uppercase;border-radius:20px;padding:0 18px;line-height:26px}
.badge{position:absolute;left:570px;width:60px;height:60px;border-radius:50%;background:#fff;box-shadow:0 2px 8px rgba(0,0,0,.12);display:flex;align-items:center;justify-content:center;font-family:var(--head);font-weight:600;font-size:18px;color:var(--orange)}

/* Hero */
.hero{top:0;height:590px;background:linear-gradient(120deg,#6b5a40 0%,#8c7a55 25%,#b99a4a 42%,#55708e 62%,#3e4f62 80%,#6f6350 100%)}
.hero::after{content:"";position:absolute;inset:0;background:rgba(20,18,16,.45)}
.hero > *{z-index:2}
.logo{position:absolute;left:128px;top:24px;color:#fff}
.logo .name{font-family:var(--body);font-size:22px;font-weight:400;line-height:24px}
.logo .tag{font-size:7px;letter-spacing:.3px;margin-left:34px}
.nav{position:absolute;top:31px;left:476px;display:flex;align-items:center;font-size:9px;font-weight:500;color:#fff;text-transform:uppercase}
.nav a{margin-right:22px;white-space:nowrap}
.nav .on{color:var(--orange)}
.nav .sep{width:1px;height:12px;background:rgba(255,255,255,.4);margin:0 14px 0 -6px}
.nav .demo{background:var(--orange);border-radius:16px;padding:0 16px;line-height:24px;margin:0 0 0 18px}
.dropdown{position:absolute;left:513px;top:56px;width:157px;background:#2a2a2a;font-size:9px;color:#fff;padding:6px 0}
.dropdown div{padding:0 12px;line-height:26px}
.dropdown .active{background:var(--orange)}
.hero-eyebrow{top:232px;font-size:9px;letter-spacing:2.5px;color:#fff;font-weight:600}
.hero-title{top:254px;font-family:var(--head);font-size:40px;font-weight:500;color:#fff;letter-spacing:.5px}
.hero-sub{top:304px;font-size:13px;color:#fff}
.hero-btn{top:342px}

/* Platforms */
.platforms{top:590px;height:391px}
.logo-grid{position:absolute;left:135px;top:200px;width:931px;display:grid;grid-template-columns:repeat(6,144px);gap:14px 13px}
.logo-tile{height:54px;background:#f2f2f2;border-radius:2px;display:flex;align-items:center;justify-content:center;font-size:15px;color:#555;font-weight:500}
.logo-tile.white{background:#fff;box-shadow:0 1px 6px rgba(0,0,0,.1)}
.logo-tile .sq{width:18px;height:18px;background:#666;margin-right:7px}
.logo-tile .shape{width:22px;height:22px;background:#777}
.logo-tile .shape.round{border-radius:50%}

/* Technology */
.tech{top:981px;height:504px}
.tech .rule{position:absolute;left:0;top:0;width:1200px;height:1px;background:var(--line)}
.tech .label{top:-6px;left:530px;width:140px;background:#fff}
.tablet{left:464px;top:67px;width:270px;height:378px;background:#1a1a1a;border-radius:16px;box-shadow:0 8px 24px rgba(0,0,0,.25)}
.tablet .screen{position:absolute;left:28px;top:30px;width:214px;height:290px;background:linear-gradient(180deg,#e6ebf2,#c7d3e6 40%,#b9a6d8 70%,#e6ebf2)}
.tablet .home{position:absolute;left:121px;top:336px;width:28px;height:28px;border-radius:50%;border:2px solid #444}
.feature{position:absolute;width:300px}
.feature h4{font-family:var(--head);font-weight:500;font-size:11px;color:var(--ink);text-transform:uppercase;line-height:15px}
.feature h4.hl{color:var(--orange)}
.feature p{font-size:9px;line-height:14px;margin-top:4px}
.feature.left{text-align:right;left:55px}
.feature.right{left:846px}
.ficon{position:absolute;width:58px;height:58px;border-radius:50%;background:#2e2e2e;display:flex;align-items:center;justify-content:center}
.ficon.hot{background:var(--orange)}

/* Why us */
.why{top:1485px;height:630px;background:var(--light)}
.why .para{top:180px;font-size:10px;line-height:15px}
.card{position:absolute;top:232px;width:221px;height:353px}
.card .label{position:absolute;left:0;width:100%;bottom:34px;text-align:center;font-family:var(--head);font-size:10px;color:#fff;letter-spacing:.5px}
.card .ico{position:absolute;left:91px;bottom:-20px;width:40px;height:40px;border-radius:50%;background:#fff;box-shadow:0 2px 6px rgba(0,0,0,.15);display:flex;align-items:center;justify-content:center}
.card.dark{background:#3a3a3a;text-align:center;color:#fff}
.card.dark h5{font-family:var(--head);font-weight:500;font-size:12px;margin-top:36px}
.card.dark p{font-size:9.5px;line-height:15px;padding:10px 30px 0;color:#ddd}
.card.dark .btn{margin-top:14px;font-size:8px;line-height:22px}
.card.dark .dot{position:absolute;left:96px;top:293px;width:30px;height:30px;border-radius:50%;background:var(--orange)}

/* ROI */
.roi{top:2115px;height:308px}
.stat{position:absolute;top:100px;width:240px;text-align:center}
.stat .circ{width:62px;height:62px;margin:0 auto;border-radius:50%;background:#f1f1f1;display:flex;align-items:center;justify-content:center}
.stat .circ.hot{background:var(--orange);color:#fff;font-family:var(--head);font-weight:600;font-size:18px}
.stat .num{font-size:26px;color:var(--orange);margin-top:14px;font-weight:400;line-height:30px}
.stat .num b{font-weight:600}
.stat p{font-size:9.5px;line-height:15px;margin-top:8px}

/* Testimonial */
.testi{top:2423px;height:471px;background:linear-gradient(180deg,#2d2d2d,#262626 60%,#2f2f2f)}
.testi .h2{color:#fff;font-size:30px}
.avatar{left:571px;top:157px;width:58px;height:58px;border-radius:50%;background:linear-gradient(160deg,#c9a58a,#7c5a48);border:2px solid var(--orange)}
.quote{top:225px;left:290px;width:620px;text-align:center;color:#fff;font-size:13px;line-height:20px}
.who{top:330px;font-size:10px;color:#fff;font-weight:600}
.role{top:346px;font-size:9px;color:#bbb}
.client-mark{left:584px;top:372px;width:32px;height:32px;background:#d3203a;border-radius:3px}
.arrow-l,.arrow-r{top:270px;color:#777;font-size:20px}

/* Industries */
.industries{top:2894px;height:467px}
.industries .para{top:132px;left:360px;width:480px;font-size:10px;line-height:15px;text-align:center}
.industry{position:absolute;top:205px;width:150px;text-align:center}
.industry .ph{width:108px;height:108px;margin:0 auto;border-radius:50%;border:4px solid #fff;box-shadow:0 2px 10px rgba(0,0,0,.15)}
.industry span{display:block;margin-top:14px;font-family:var(--head);font-size:11px;color:var(--ink);text-transform:uppercase}
.industry.on span{color:var(--orange)}
.industry.on .ph{border-color:var(--orange);background:var(--orange);color:#fff;display:flex;flex-direction:column;align-items:center;justify-content:center;font-size:8px;line-height:11px}
.industry.on .ph b{font-size:11px}

/* Video */
.video{top:3361px;height:410px;background:var(--light)}
.video-img{left:130px;top:64px;width:460px;height:306px;background:linear-gradient(135deg,#e4e2dd,#bfb7ab 45%,#7d6450 60%,#d9d6d0)}
.play{left:566px;top:193px;width:48px;height:48px;border-radius:50%;background:#fff;box-shadow:0 2px 8px rgba(0,0,0,.2);display:flex;align-items:center;justify-content:center}
.video h3{position:absolute;left:648px;top:90px;font-family:var(--head);font-weight:500;font-size:33px;line-height:37px;color:var(--ink)}
.video .kicker{left:648px;top:68px}
.video .p1{left:648px;top:208px;width:340px;font-size:10px;line-height:15px}
.video .p2{left:648px;top:244px;width:340px;font-size:10px;line-height:15px}
.video .vbtn{left:648px;top:310px}

/* Trend setters */
.trend{top:3771px;height:229px}
.brand-row{position:absolute;left:164px;top:99px;display:flex;gap:10px}
.brand{width:166px;height:54px;background:#f2f2f2;display:flex;align-items:center;justify-content:center;font-size:15px;font-weight:600;color:#555}
.brand.white{background:#fff;box-shadow:0 1px 6px rgba(0,0,0,.1);font-size:11px}
.brand .sq{width:16px;height:16px;background:#555;margin-right:6px}
.trend .arr{top:110px;font-size:22px;color:#bbb}

/* CTA */
.cta{top:4000px;height:293px;background:linear-gradient(100deg,#3a3f45 0%,#4b5058 35%,#8a6a3a 65%,#c98f2c 85%,#7a5a2e 100%)}
.cta::after{content:"";position:absolute;inset:0;background:rgba(25,25,25,.55)}
.cta > *{z-index:2}
.cta .h2{color:#fff;font-size:30px}
.cta .para{top:135px;left:370px;width:460px;text-align:center;font-size:10px;line-height:15px;color:#eee}
.cta .btns{top:200px;display:flex;justify-content:center;gap:10px}
.btn.ghost{background:#fff;color:#333}

/* Footer */
.footer{top:4293px;height:340px;background:var(--darker);color:#bbb;font-size:9px;line-height:15px}
.footer .flogo{left:158px;top:68px;color:#fff}
.footer .flogo .name{font-size:22px;line-height:24px}
.footer .flogo .tag{font-size:7px;margin-left:32px}
.follow{left:214px;top:112px;font-size:8px}
.socials{left:196px;top:132px;display:flex;gap:10px}
.socials span{width:20px;height:20px;border-radius:50%;border:1px solid #666}
.fcol{position:absolute;top:66px}
.fcol h6{font-family:var(--body);font-size:8px;font-weight:600;color:#fff;text-transform:uppercase;letter-spacing:.5px;margin-bottom:14px}
.fcol .hl{color:var(--orange)}
.news{left:869px;width:200px}
.news .field{margin-top:12px;height:26px;border-radius:14px;background:#333;padding:0 12px;line-height:26px;color:#777;font-size:8px}
.fbottom{left:130px;top:305px;width:940px;display:flex;justify-content:space-between;font-size:8px}
.fbottom .links span{margin-left:22px}
</style>
</head>
<body>

<!-- Hero -->
<header class="section hero">
  <div role="img" aria-label="Photo of two construction workers in hard hats reviewing plans on site" class="abs" style="inset:0;z-index:1"></div>
  <div class="logo"><div class="name">QuillbarnDocs</div><div class="tag">The Ultimate Construction Technology</div></div>
  <nav class="nav">
    <a class="on">Home</a><a class="on">What We Offer ▾</a><a>Portfolio</a><a>About ▾</a><a>Blog</a><a>Contact</a>
    <span class="sep"></span><a>Login</a><a class="demo">Schedule a Demo</a>
  </nav>
  <div class="dropdown"><div>QuillbarnDocs</div><div class="active">QuillbarnCost</div><div>SubmitDesk</div><div>Project Closeouts</div></div>
  <div class="abs center hero-eyebrow">SAFEGUARDED AGAINST LITIGATION</div>
  <h1 class="abs center hero-title">THE SMARTEST WAY TO BUILD</h1>
  <div class="abs center hero-sub">Construction management software with human integration</div>
  <div class="abs center hero-btn"><span class="btn">Explore More</span></div>
</header>

<!-- Platforms -->
<section class="section platforms">
  <div class="abs center eyebrow" style="top:68px">We Improve All</div>
  <h2 class="abs center h2" style="top:88px">Construction Management<br><span class="accent">Software Platforms</span></h2>
  <div class="logo-grid">
    <div class="logo-tile">Stackline</div>
    <div class="logo-tile">Corvex</div>
    <div class="logo-tile white"><span class="sq"></span>Bimfold 360</div>
    <div class="logo-tile">Tarrow</div>
    <div class="logo-tile">Plankway</div>
    <div class="logo-tile">Ferrix</div>
    <div class="logo-tile">Beamhill</div>
    <div class="logo-tile">Crewtable</div>
    <div class="logo-tile">Pinboardly</div>
    <div class="logo-tile"><span class="shape"></span></div>
    <div class="logo-tile"><span class="shape round"></span></div>
    <div class="logo-tile"><span class="shape round"></span></div>
  </div>
</section>

<!-- Technology -->
<section class="section tech">
  <div class="rule"></div>
  <div class="abs eyebrow label" style="text-align:center">Technology</div>
  <div class="abs tablet">
    <div class="screen" role="img" aria-label="Screenshot of the scheduling dashboard"></div>
    <div class="home"></div>
  </div>

  <div class="feature left" style="top:112px"><h4>Third-Party Custodian<br>of Project Information</h4><p>Lorem Ipsum is simply dummy text of the printing and typesetting industry. Lorem Ipsum has been the industry's standard dummy text</p></div>
  <div class="ficon" style="left:374px;top:112px"><svg width="20" height="20" viewBox="0 0 24 24" fill="none" stroke="#EE7325" stroke-width="2"><path d="M12 2l8 4v6c0 5-3.5 8.5-8 10-4.5-1.5-8-5-8-10V6z"/><path d="M8.5 12l2.5 2.5 4.5-5"/></svg></div>

  <div class="feature left" style="top:212px"><h4>Dedicated Project<br>Information Manager</h4><p>Lorem Ipsum is simply dummy text of the printing and typesetting industry. Lorem Ipsum has been the industry's standard dummy text</p></div>
  <div class="ficon" style="left:374px;top:212px"><svg width="18" height="20" viewBox="0 0 20 24" fill="none" stroke="#EE7325" stroke-width="2"><path d="M3 2h10l4 4v16H3z"/><path d="M7 11h6M7 15h6"/></svg></div>

  <div class="feature left" style="top:329px"><h4>Digital Governance</h4><p>Lorem Ipsum is simply dummy text of the printing and typesetting industry. Lorem Ipsum has been the industry's standard dummy text</p></div>
  <div class="ficon" style="left:374px;top:316px"><svg width="20" height="20" viewBox="0 0 24 24" fill="none" stroke="#EE7325" stroke-width="2"><path d="M3 9l9-5 9 5M5 9v10M10 9v10M14 9v10M19 9v10M3 21h18"/></svg></div>

  <div class="ficon" style="left:768px;top:112px"><svg width="20" height="20" viewBox="0 0 24 24" fill="none" stroke="#EE7325" stroke-width="2"><path d="M12 2l8 4v6c0 5-3.5 8.5-8 10-4.5-1.5-8-5-8-10V6z"/><path d="M12 8v5M12 16v.5"/></svg></div>
  <div class="feature right" style="top:112px"><h4>Risk Mitigation</h4><p>Lorem Ipsum is simply dummy text of the printing and typesetting industry. Lorem Ipsum has been the industry's standard dummy text</p></div>

  <div class="ficon hot" style="left:768px;top:212px"><svg width="18" height="20" viewBox="0 0 20 24" fill="none" stroke="#fff" stroke-width="2"><path d="M3 2h10l4 4v16H3z"/><path d="M7 14l2 2 4-5"/></svg></div>
  <div class="feature right" style="top:212px"><h4 class="hl">Audited and<br>Vetted Documentation</h4><p>Lorem Ipsum is simply dummy text of the printing and typesetting industry. Lorem Ipsum has been the industry's standard dummy text</p></div>

  <div class="ficon" style="left:768px;top:316px"><svg width="20" height="20" viewBox="0 0 24 24" fill="none" stroke="#EE7325" stroke-width="2"><circle cx="12" cy="12" r="3.5"/><path d="M12 2v3M12 19v3M2 12h3M19 12h3M4.9 4.9l2.1 2.1M17 17l2.1 2.1M4.9 19.1L7 17M17 7l2.1-2.1"/></svg></div>
  <div class="feature right" style="top:329px"><h4>Digital Twin Integration<br>for Facilities Management</h4><p>Lorem Ipsum is simply dummy text of the printing and typesetting industry. Lorem Ipsum has been the industry's standard dummy text</p></div>
</section>

<!-- Why us -->
<section class="section why">
  <div class="badge" style="top:-26px">QD</div>
  <div class="abs center eyebrow" style="top:71px">Why We Are The</div>
  <h2 class="abs center h2" style="top:92px">Best Construction<br><span class="accent">Management Software</span></h2>
  <div class="abs para" style="left:360px;width:480px;text-align:center">Lorem Ipsum is simply dummy text of the printing and typesetting industry. Lorem Ipsum has been the industry's standard dummy text ever since the 1500s</div>

  <div class="card" style="left:130px;background:linear-gradient(160deg,#9fb3c6,#4d6a88 55%,#2b3d52)" role="img" aria-label="Photo of a person using a tablet with data charts">
    <div class="label">INFORMATION MANAGER</div>
    <div class="ico"><svg width="14" height="16" viewBox="0 0 20 24" fill="none" stroke="#555" stroke-width="2"><path d="M3 2h10l4 4v16H3z"/><path d="M7 12h6M7 16h6"/></svg></div>
  </div>
  <div class="card dark" style="left:369px">
    <h5>INTEGRATION ACROSS THE BOARD</h5>
    <p>Lorem Ipsum is simply dummy text of the printing and typesetting industry. Lorem Ipsum has been the industry's standard dummy text ever since the 1500s, when an unknown printer took a galley of type and scrambled it to make a type specimen book.</p>
    <span class="btn">Ask Us How</span>
    <div class="dot"></div>
  </div>
  <div class="card" style="left:610px;background:linear-gradient(180deg,#1d3a6b,#2a5aa0 45%,#0d1f3d)" role="img" aria-label="Photo of a server room corridor">
    <div class="label">DATA-DRIVEN</div>
    <div class="ico"><svg width="16" height="16" viewBox="0 0 24 24" fill="none" stroke="#555" stroke-width="2"><circle cx="10" cy="8" r="4"/><path d="M3 21c0-4 3-6 7-6M16 15l2 2 4-4"/></svg></div>
  </div>
  <div class="card" style="left:850px;background:linear-gradient(150deg,#e4e4e4,#bdbdbd 50%,#7e7e7e)" role="img" aria-label="Photo of hands typing on a laptop over drawings">
    <div class="label">DIGITAL TWIN</div>
    <div class="ico"><svg width="14" height="16" viewBox="0 0 20 24" fill="none" stroke="#555" stroke-width="2"><rect x="3" y="3" width="14" height="18"/><path d="M7 9h6M7 13h6"/></svg></div>
  </div>
</section>

<!-- ROI -->
<section class="section roi">
  <div class="abs center eyebrow" style="top:34px">Return on Investment</div>
  <div class="stat" style="left:120px"><div class="circ"><svg width="22" height="22" viewBox="0 0 24 24" fill="none" stroke="#666" stroke-width="1.6"><path d="M6 3h12l4 6-10 12L2 9z"/><path d="M2 9h20M12 21L8 9l4-6 4 6z"/></svg></div><div class="num">$<b>1</b>M</div><p>$1 Million of Coverage for<br>PreDiscovery for Litigation Expenses</p></div>
  <div class="stat" style="left:360px"><div class="circ hot">QD</div><div class="num"><b>18</b></div><p>On Average, you will obtain an 18 to 1<br>ROI for Every Dollar Spent</p></div>
  <div class="stat" style="left:600px"><div class="circ"><svg width="22" height="22" viewBox="0 0 24 24" fill="none" stroke="#666" stroke-width="1.6"><rect x="3" y="4" width="18" height="17"/><path d="M3 9h18M8 2v4M16 2v4M7 13h2M11 13h2M15 13h2M7 17h2M11 17h2"/></svg></div><div class="num"><b>93.3</b>%</div><p>Project will Average on Budget and<br>on Schedule 93.3% of the Time</p></div>
  <div class="stat" style="left:840px"><div class="circ"><svg width="20" height="22" viewBox="0 0 20 24" fill="none" stroke="#666" stroke-width="1.6"><rect x="2" y="3" width="16" height="19"/><path d="M6 2h8v3H6zM6 11l2 2 4-4M6 17h8"/></svg></div><div class="num"><b>6.4</b>%</div><p>6.4% of our Projects Complete<br>Ahead of Schedule</p></div>
</section>

<!-- Testimonials -->
<section class="section testi">
  <div role="img" aria-label="Faint city skyline backdrop" class="abs" style="inset:0;opacity:.15;background:linear-gradient(0deg,#555 0%,transparent 70%)"></div>
  <div class="abs center eyebrow" style="top:66px">Testimonials</div>
  <h2 class="abs center h2" style="top:84px">What Our Clients Say</h2>
  <div class="abs avatar" role="img" aria-label="Portrait of the client"></div>
  <p class="abs quote">“QuillbarnDocs was essential to the success of Harlow Mega project. The interest cost on $500m of construction financing was significant - each day made A difference. Any alternative strategy to build with clean data would result in data disasters. than QuillbarnDocs. The QuillbarnDocs solution - their people and technology – worked well.”</p>
  <div class="abs center who">Marcus T. Ellery</div>
  <div class="abs center role">Project Manager, Midland Federal Region</div>
  <div class="abs client-mark"></div>
  <div class="abs arrow-l" style="left:212px">‹</div>
  <div class="abs arrow-r" style="left:976px">›</div>
</section>

<!-- Industries -->
<section class="section industries">
  <div class="badge" style="top:-30px">QD</div>
  <div class="abs center eyebrow" style="top:65px">Portfolio</div>
  <h2 class="abs center h2" style="top:88px">Industries <span class="accent">Served</span></h2>
  <p class="abs para">Our clients encompass a wide range of industries. We work with Airports, Universities, Government Projects, Transportation, Mixed-Use, Schools, and Hospitals. The one thing they all have in common, is they all have positive things to say about QuillbarnDocs.</p>
  <div class="industry" style="left:132px"><div class="ph" role="img" aria-label="Photo of a person working at a laptop" style="background:linear-gradient(160deg,#eee,#b5b5b5 60%,#6a6a6a)"></div><span>Aviation</span></div>
  <div class="industry" style="left:290px"><div class="ph" role="img" aria-label="Photo of a modern hospital building at dusk" style="background:linear-gradient(180deg,#4d6ea0,#3b3b3b 60%,#7a5b33)"></div><span>Healthcare</span></div>
  <div class="industry" style="left:447px"><div class="ph" role="img" aria-label="Photo of a transit station with a curved roof" style="background:linear-gradient(180deg,#9cc3e0,#e8e8e8 55%,#7d8a6a)"></div><span>Transportation</span></div>
  <div class="industry on" style="left:604px"><div class="ph"><b>35</b>COMPANIES</div><span>Government</span></div>
  <div class="industry" style="left:762px"><div class="ph" role="img" aria-label="Photo of a mixed-use apartment building" style="background:linear-gradient(180deg,#cfe0ea,#8a8a86 50%,#4f6a44)"></div><span>Mixed Use</span></div>
  <div class="industry" style="left:919px"><div class="ph" role="img" aria-label="Photo of a modern school building" style="background:linear-gradient(180deg,#bcd6ea,#ececec 50%,#6d8a58)"></div><span>Education</span></div>
  <div class="abs center" style="top:374px"><span class="btn">View All Projects</span></div>
</section>

<!-- Video -->
<section class="section video">
  <div class="abs video-img" role="img" aria-label="Photo of hands holding a phone over paperwork at a desk"></div>
  <div class="abs play"><svg width="14" height="14" viewBox="0 0 24 24" fill="none" stroke="#EE7325" stroke-width="2"><path d="M7 4l13 8-13 8z"/></svg></div>
  <div class="abs eyebrow kicker">Video</div>
  <h3>Bridge the Gap in<br>Project Management<br>Software</h3>
  <p class="abs p1">Transform your next project with Document Verified and Organized with certainty!</p>
  <p class="abs p2">QuillbarnDocs tracks organizes and achieves all data to include, emails, weather, plans ( linked) planlinc, submittals, RFI, inspection reports, to include audit ready delivery.</p>
  <div class="abs vbtn"><span class="btn">More About Us</span></div>
</section>

<!-- Trend setters -->
<section class="section trend">
  <div class="abs center eyebrow" style="top:21px">Trend Setters</div>
  <div class="abs arr" style="left:127px">‹</div>
  <div class="brand-row">
    <div class="brand">Harrowell</div>
    <div class="brand white"><span class="sq"></span>KESTREL &amp; VALE</div>
    <div class="brand" style="color:#aaa;font-weight:400">Norbury</div>
    <div class="brand" style="font-size:11px;font-weight:500">PELLAM GROUP</div>
    <div class="brand"><span class="sq" style="border-radius:50%"></span>CRESTMOOR</div>
  </div>
  <div class="abs arr" style="left:1060px">›</div>
</section>

<!-- CTA -->
<section class="section cta">
  <div role="img" aria-label="Photo of construction workers in hard hats and safety vests" class="abs" style="inset:0;z-index:1"></div>
  <div class="badge" style="top:-30px;z-index:3">QD</div>
  <div class="abs center eyebrow" style="top:64px">Contact</div>
  <h2 class="abs center h2" style="top:82px">We Are Here To Help</h2>
  <p class="abs para">Using our array of services, you can finally alleviate the stress of managing large construction projects. Find out how QuillbarnDocs solves the largest problems in project management and how you can benefit.</p>
  <div class="abs center btns" style="width:1200px;left:0"><span class="btn">✉ Contact Us</span><span class="btn ghost">☏ (555) 310-4827</span></div>
</section>

<!-- Footer -->
<footer class="section footer">
  <div class="abs flogo"><div class="name">QuillbarnDocs</div><div class="tag">The Ultimate Construction Technology</div></div>
  <div class="abs follow">Follow Us</div>
  <div class="abs socials"><span></span><span></span><span></span></div>
  <div class="fcol" style="left:369px"><h6>About</h6>About Us<br>Portfolio<br>Articles &amp; Press<br>Events<br>Podcast<br>Blog<br>Contact Us</div>
  <div class="fcol" style="left:490px"><h6>What We Offer</h6>QuillbarnDocs<br><span class="hl">QuillbarnCost</span><br>SubmitDesk<br>Project Closeouts</div>
  <div class="fcol" style="left:610px"><h6>How We Work</h6>Owners /<br>Shareholders<br>Contractors<br>Construction Lawyers<br>Finance</div>
  <div class="fcol" style="left:729px"><h6>Contact</h6>Address:<br>412 Larkfield Ave<br>Riverton, MO 64110<br>Phone:<br>(555) 310-4827<br>Email:<br>hello@quillbarn.com<br>support@quillbarn.com</div>
  <div class="fcol news"><h6>Newsletter</h6>Subscribe to our emailing list. Lorem Ipsum is simply dummy text of the printing and typesetting industry.<div class="field">Your Email Address</div></div>
  <div class="abs fbottom"><span>© Copyright 2022 QuillbarnDocs. All Rights Reserved</span><span class="links"><span>PRIVACY POLICY</span><span>TERMS &amp; CONDITIONS</span><span>DISCLAIMER</span></span></div>
</footer>

</body>
</html>
```